Borrowed Lanterns - the new thriller in the Tidewater series by award-winning author Marta K. Belloway

Looking for an book cover design for the 4th book in the Tidewater series by Marta K. Belloway. Covers from the first 3 books are attached. Would like to keep a series look going, so possibly using a hand holding a paint brush might work - but not tied down to showing a hand on the cover. Most of the book takes place in a rustic Arizona desert estate in a national forest - so something depicting a desert scene might work too. The cover needs to convey a "thriller" feeling. Attached is our design template with needed specs. Also attached are two other covers for inspiration:

A GARDEN UNDER SALT - something like this could work in the key were a paintbrush and the scene is set in the Arizona desert

THE ORCHARD AT NOON - this could work too with Arizona desert setting

Here's the synopsis of BORROWED LANTERNS:

Her life ended and she is disappointed to discover she is still alive.

With all ties to her handler or anyone connected to her life as a hired killer, she struggles to understand who and even what she has become. She knows she doesn’t want to kill again. And yes, danger finds her and she responds, animal-like, in the only way she knows how.

In this mood of absolute bereavement, she comes across Harriet Vasquell, a world famous artist who has spent the last three decades living a hermit-like existence on a rustic desert estate in a national forest.

Harriet invites her to stay on to assist the old woman who will, in return, mentor our narrator as she deepens her own interest in art.

What is not at first apparent is that elements of Harriet’s past are shrouded in danger, sorrow and darkness and rather than growing as an artist, she soon finds herself enmeshed in a dangerous mystery with strands that stretch decades into the past.

```html
<!DOCTYPE html>
<html lang="en">
<head>
<meta charset="utf-8">
<title>Borrowed Lanterns — Marta K. Belloway</title>
<link rel="stylesheet" href="https://fonts.googleapis.com/css2?family=Bebas+Neue&family=Montserrat:wght@400&display=swap">
<style>
  :root {
    --bg: #2c2c2c;
    --bg-light: #363636;
    --title-red: #f50a0a;
    --hand-red: #e0140e;
    --hand-dark: #7a0805;
    --white: #ffffff;
  }
  html, body {
    margin: 0;
    padding: 0;
    width: 766px;
    height: 1200px;
    overflow: hidden;
    background: var(--bg);
  }
  .cover {
    position: relative;
    width: 766px;
    height: 1200px;
    overflow: hidden;
    background:
      radial-gradient(ellipse 320px 200px at 20% 30%, var(--bg-light), transparent 70%),
      radial-gradient(ellipse 280px 220px at 80% 65%, var(--bg-light), transparent 70%),
      radial-gradient(ellipse 260px 180px at 35% 85%, var(--bg-light), transparent 70%),
      var(--bg);
  }
  .title {
    position: absolute;
    left: 0;
    top: 44px;
    width: 100%;
    margin: 0;
    text-align: center;
    font-family: "Bebas Neue", "Oswald", sans-serif;
    font-weight: 400;
    font-size: 210px;
    line-height: 216px;
    color: var(--title-red);
    letter-spacing: 1px;
  }
  .title span { display: block; }
  .tagline {
    position: absolute;
    left: 504px;
    top: 486px;
    margin: 0;
    font-family: "Montserrat", sans-serif;
    font-weight: 400;
    font-size: 35px;
    letter-spacing: 1px;
    color: var(--white);
    white-space: nowrap;
  }
  .hand-art {
    position: absolute;
    left: 40px;
    top: 580px;
    width: 726px;
    height: 316px;
    background: linear-gradient(100deg, rgba(122,8,5,0) 0%, var(--hand-dark) 30%, var(--hand-red) 60%, var(--hand-red) 100%);
    border-radius: 0 0 0 160px;
    opacity: 0.85;
  }
  .author {
    position: absolute;
    left: 0;
    top: 1046px;
    width: 100%;
    margin: 0;
    text-align: center;
    font-family: "Bebas Neue", "Oswald", sans-serif;
    font-weight: 400;
    font-size: 112px;
    line-height: 112px;
    color: var(--white);
    letter-spacing: 2px;
    white-space: nowrap;
  }
</style>
</head>
<body>
  <main class="cover">
    <h1 class="title"><span>Borrowed</span><span>Lanterns</span></h1>
    <p class="tagline">A NOVEL</p>
    <div class="hand-art" role="img" aria-label="Red-tinted hand reaching in from the right, holding a dark paintbrush"></div>
    <p class="author">MARTA K. BELLOWAY</p>
  </main>
</body>
</html>
```